Label Design for Bra "Heron Lingerie" by Tamsel Apparel Company

The bra is packaged in a poly bag with a hanger. We require a label design for the brand name "Heron Lingerie" by Tamsel Apparel Company. The main label will be attached by a string on the bra. The size of that label will 25cm in length and 10cm wide. This is the first label the customer see's when she picks up the garment/bra. Therefore, we require an eye catching design for that. This classic full shape bra with smooth moulded double layered cups fit beautifully under t-shirts and fitted garments. The tamsel apparel company logo has been included and we would like it to feature in the label. A sample labels are also given.
Target Market(s)
Laddies 18 - 45
Industry/Entity Type
Clothing
Look and feel
Each slider illustrates characteristics of the customer's brand and the style your logo design should communicate.

```html
<!DOCTYPE html>
<html lang="en">
<head>
<meta charset="utf-8">
<title>Heron Lingerie – Hang Tag</title>
<link rel="stylesheet" href="https://fonts.googleapis.com/css2?family=Cinzel:wght@600;700;800&display=swap">
<style>
  :root {
    --backdrop: #000000;
    --plum: #9f446d;
    --rose: #c4467f;
    --magenta: #d94a90;
    --white: #ffffff;
    --orange: #f7941d;
  }
  html, body {
    margin: 0;
    padding: 0;
    width: 1200px;
    height: 1200px;
    overflow: hidden;
    background: var(--backdrop);
  }
  .canvas {
    position: relative;
    width: 1200px;
    height: 1200px;
    background: var(--backdrop);
    font-family: "Cinzel", "Times New Roman", serif;
    color: var(--white);
  }
  .hang-tag {
    position: absolute;
    left: 409px;
    top: 147px;
    width: 367px;
    height: 919px;
    overflow: hidden;
  }
  .tag-body {
    position: absolute;
    left: 0;
    top: 0;
    width: 367px;
    height: 704px;
    background: linear-gradient(215deg, var(--plum) 0%, var(--rose) 50%, var(--magenta) 100%);
  }
  .brand-name {
    position: absolute;
    left: 0;
    width: 367px;
    top: 155px;
    text-align: center;
    font-weight: 700;
    font-size: 56px;
    line-height: 1;
    letter-spacing: 2px;
  }
  .figure-art {
    position: absolute;
    left: 13px;
    top: 270px;
    width: 180px;
    height: 390px;
    border-radius: 50%;
    background: radial-gradient(ellipse at center, rgba(255,255,255,0.10) 0%, rgba(255,255,255,0) 70%);
  }
  .features {
    list-style: none;
    margin: 0;
    padding: 0;
  }
  .feature {
    position: absolute;
    display: flex;
    align-items: center;
    font-weight: 700;
    font-size: 17px;
    line-height: 1;
    white-space: nowrap;
    font-variant: small-caps;
  }
  .feature::before {
    content: "";
    width: 15px;
    height: 15px;
    border-radius: 50%;
    background: var(--white);
    margin-right: 5px;
  }
  .feature--fit { left: 166px; top: 449px; }
  .feature--wrinkle { left: 137px; top: 482px; }
  .feature--wash { left: 123px; top: 517px; }
  .feature--fabric { left: 153px; top: 553px; }
  .divider-band {
    position: absolute;
    left: 0;
    top: 704px;
    width: 367px;
    height: 35px;
    background: var(--white);
  }
  .slogan-panel {
    position: absolute;
    left: 0;
    top: 739px;
    width: 367px;
    height: 180px;
    background: var(--orange);
    text-align: center;
    font-weight: 700;
  }
  .slogan-top {
    position: absolute;
    left: 0;
    width: 367px;
    top: 14px;
    font-size: 60px;
    line-height: 1;
  }
  .slogan-bottom {
    position: absolute;
    left: 0;
    width: 367px;
    top: 90px;
    font-size: 82px;
    line-height: 1;
  }
</style>
</head>
<body>
<div class="canvas">
  <div class="hang-tag">
    <div class="tag-body">
      <div class="brand-name">heron</div>
      <div class="figure-art" role="img" aria-label="Abstract line outline of a female figure"></div>
      <ul class="features">
        <li class="feature feature--fit">Comfort Fit</li>
        <li class="feature feature--wrinkle">Wrinkle -Resistant</li>
        <li class="feature feature--wash">MACHINE wASHABLE</li>
        <li class="feature feature--fabric">LUXURY fABRIC</li>
      </ul>
    </div>
    <div class="divider-band"></div>
    <div class="slogan-panel">
      <div class="slogan-top">BEAUTY</div>
      <div class="slogan-bottom">INSIDE</div>
    </div>
  </div>
</div>
</body>
</html>
```